Korvex Global ltd. Stationaries
Full Stationary set
Korvex Global ltd. Stationaries  -
Creative Brief
Professional
Owen Pallister
VP, Sales MENA
Korvex Global Limited Zerhani Tower Office No. 614-616, 6th Floor Qasr Nadeem Road, Hessa P.O. Box 4827 Dubai, UAE
owen.pallister@korvexglb.example
korvexglb.example
All Size A4 (European Size) - Letterhead (Word Template, PDF, AI) - Purchase Order (Excel Template, PDF, AI) - Quotation (Excel Template, PDF, AI) - Invoice (Excel Template, PDF, AI) - Envelope (Big, Medium, Small) - Business Card (front and back) - Power Point Template - CD/DVD (label and jacket) - Folder
Broadcasting Solutions

```html
<!DOCTYPE html>
<html lang="en">
<head>
<meta charset="utf-8">
<title>Korvex Global ltd. – Business Card</title>
<link href="https://fonts.googleapis.com/css2?family=Arimo:ital,wght@0,400;0,700;1,700&family=Tinos&display=swap" rel="stylesheet">
<style>
  :root {
    --backdrop: #d9d9d9;
    --card-white: #ffffff;
    --panel-dark: #3a3a3a;
    --panel-darker: #2b2b2b;
    --panel-edge: #6a6a6a;
    --text-light: #f2f2f2;
    --text-soft: #d4d4d4;
    --brand-ink: #3c3c3c;
    --brand-dot: #1f7fc4;
  }
  html, body {
    margin: 0;
    width: 1200px;
    height: 780px;
    overflow: hidden;
    background: var(--backdrop);
  }
  .business-card {
    position: absolute;
    left: 100px;
    top: 105px;
    width: 1000px;
    height: 570px;
    border-radius: 30px;
    overflow: hidden;
    display: flex;
    box-shadow: 0 10px 30px rgba(0,0,0,0.18);
  }
  .card-brand-side {
    width: 440px;
    background: var(--card-white);
    display: flex;
    align-items: center;
    justify-content: center;
  }
  .brand-lockup {
    display: flex;
    align-items: center;
    gap: 16px;
    margin-top: 40px;
  }
  .brand-dot {
    width: 44px;
    height: 44px;
    border-radius: 50%;
    background: var(--brand-dot);
  }
  .brand-name {
    font-family: "Arimo", sans-serif;
    font-weight: 700;
    font-size: 34px;
    color: var(--brand-ink);
    letter-spacing: -0.5px;
  }
  .card-contact-side {
    position: relative;
    flex: 1;
    background: linear-gradient(135deg, var(--panel-dark) 0%, var(--panel-darker) 100%);
    border-left: 4px solid var(--panel-edge);
    color: var(--text-soft);
    text-align: right;
    padding: 0 46px;
  }
  .holder-name {
    margin: 34px 0 0;
    font-family: "Arimo", sans-serif;
    font-weight: 700;
    font-style: italic;
    font-size: 31px;
    color: var(--text-light);
  }
  .holder-title {
    margin: 4px 0 0;
    font-family: "Arimo", sans-serif;
    font-size: 20px;
    color: var(--text-light);
  }
  .office-address {
    margin: 118px 0 0;
    font-family: "Tinos", serif;
    font-style: normal;
    font-size: 23px;
    line-height: 31px;
  }
  .contact-list {
    list-style: none;
    margin: 26px 0 0;
    padding: 0;
    font-family: "Tinos", serif;
    font-size: 23px;
    line-height: 36px;
  }
  .contact-list li {
    display: flex;
    justify-content: flex-end;
    align-items: center;
    gap: 12px;
  }
  .contact-icon {
    width: 20px;
    height: 20px;
    flex: none;
  }
</style>
</head>
<body>
  <div class="business-card">
    <section class="card-brand-side">
      <div class="brand-lockup">
        <span class="brand-dot"></span>
        <span class="brand-name">Korvex Global ltd.</span>
      </div>
    </section>
    <section class="card-contact-side">
      <p class="holder-name">Owen Pallister</p>
      <p class="holder-title">VP, Sales MENA</p>
      <address class="office-address">
        4471 - 19 Street, Calderon,<br>
        Westmark, K2P 7D4 Zerhani Tower<br>
        Office No. 614-616, 6th Floor<br>
        Qasr Nadeem Road, Hessa<br>
        P.O. Box 4827, Dubai, UAE
      </address>
      <ul class="contact-list">
        <li>+971 504816270
          <svg class="contact-icon" viewBox="0 0 20 20" aria-hidden="true"><path d="M5 2l3 3-2 2c1 3 3 5 6 6l2-2 3 3-2 3C8 17 3 12 2 5z" fill="#d4d4d4"/></svg>
        </li>
        <li>owen.pallister@korvexglb.example
          <svg class="contact-icon" viewBox="0 0 20 20" aria-hidden="true"><circle cx="10" cy="10" r="4" fill="none" stroke="#d4d4d4" stroke-width="2"/><path d="M14 7v5c0 2 3 2 3-1a7 7 0 1 0-3 6" fill="none" stroke="#d4d4d4" stroke-width="2"/></svg>
        </li>
        <li>www.korvexglb.example
          <svg class="contact-icon" viewBox="0 0 20 20" aria-hidden="true"><circle cx="10" cy="10" r="8" fill="none" stroke="#d4d4d4" stroke-width="1.6"/><ellipse cx="10" cy="10" rx="3.5" ry="8" fill="none" stroke="#d4d4d4" stroke-width="1.4"/><path d="M2 10h16" stroke="#d4d4d4" stroke-width="1.4"/></svg>
        </li>
      </ul>
    </section>
  </div>
</body>
</html>
```